vascular clinic webdesign (wordpress+neve theme+ elementor)

Create a nice webdesign for an existing website of a vascular surgery clinic. Vascular surgery is the medical specialty that treats arteries and veins. Content should not change. First landing page we can recreate content if needed, but internal pages should not change content. We currently use Neve theme (https://brovanta.com/themes/kelto/) in a Wordpress CMS, which is highly customizable, we prefer to keep using it, as it is standard in all our sites, and will be often upgraded. We also have Elementor Pro. Please visit current domain: quintela.pro.
Page is in portuguese. But you can do anything in English that I translate later, or you can use original domain content already in portuguese.
Selected design need to be coded in wordpress+neve+elementor

Minimum pages:
First Page/Landing page (https://quintela.pro/)
Contact page (https://quintela.pro/contato/)
Post/Article page
About us (https://quintela.pro/a-clinica/)
Posts Archive (https://quintela.pro/todos-artigos/)
The team (https://quintela.pro/sobre-nos-equipe-de-cirurgia-vascular-endovascular-ecografia-angiologia/)

Designs look the same

Target Market(s)

mostly (70%) woman, 30 to 60 years

Industry/Entity Type

Health

Coding

Coded - Design and coding required

Number of Pages Required

5+ page

Font styles to use
Serif

Requirements
Should not have
• Will not change Wordpress for any other CMS
Prefer not to change theme Neve (https://brovanta.com/themes/kelto/)

```html
<!DOCTYPE html>
<html lang="en">
<head>
<meta charset="utf-8">
<title>The Team — Quintela.pro</title>
<link href="https://fonts.googleapis.com/css2?family=Open+Sans:wght@300;400;600;700&family=Cormorant+Garamond:wght@500;600&display=swap" rel="stylesheet">
<style>
:root{
  --maroon:#7b1d1d;
  --maroon-dark:#5a1212;
  --blue:#2f78b8;
  --ink:#333;
  --muted:#6b6b6b;
  --line:#d9d9d9;
  --footer:#231f20;
  --hero-a:#b9c7d3;
  --hero-b:#e7edf2;
}
*{box-sizing:border-box;margin:0;padding:0}
html,body{width:1200px;height:3792px;overflow:hidden}
body{font-family:"Open Sans",sans-serif;color:var(--ink);background:#fff;position:relative;font-size:15px}
a{color:inherit;text-decoration:none}
.brand{font-family:"Cormorant Garamond",serif;font-weight:600;font-size:40px;color:var(--maroon);letter-spacing:1px}

/* header */
.site-header{position:absolute;top:0;left:0;width:1200px;height:92px;background:#fff;z-index:3}
.site-header .brand{position:absolute;left:40px;top:22px}
.topbar{position:absolute;right:40px;top:10px;font-size:13px;color:var(--ink);display:flex;gap:22px;align-items:center}
.topbar span{display:flex;align-items:center;gap:6px}
.ico{width:14px;height:14px;fill:var(--maroon)}
.main-nav{position:absolute;right:40px;top:50px;display:flex;gap:22px;font-size:14px;font-weight:600;text-transform:uppercase;color:#444}
.main-nav .current{color:var(--maroon)}

/* hero */
.hero{position:absolute;top:92px;left:0;width:1200px;height:420px;background:linear-gradient(120deg,var(--hero-a),var(--hero-b) 60%,#cfd9e2)}
.hero h1{position:absolute;left:40px;top:140px;font-family:"Cormorant Garamond",serif;font-size:80px;font-weight:600;color:#fff;letter-spacing:3px}
.hero .dots{position:absolute;left:572px;top:252px;display:flex;gap:8px}
.hero .dots i{width:10px;height:10px;border-radius:50%;background:#fff;opacity:.6}
.hero .dots i:first-child{opacity:1}
.hero svg.curve{position:absolute;left:0;bottom:-2px;width:1200px;height:120px}

/* team intro */
.team-intro{position:absolute;top:548px;left:0;width:1200px;text-align:center}
.section-title{font-size:46px;font-weight:300;text-transform:uppercase;color:var(--ink);letter-spacing:1px}
.section-title b{font-weight:600;color:var(--maroon)}
.team-intro h2{font-size:22px;font-weight:600;margin-top:10px;color:#222}
.team-intro p{font-size:14px;color:var(--muted);line-height:1.75;width:1000px;margin:14px auto 0}

/* featured */
.featured{position:absolute;top:872px;left:220px;width:880px;height:390px}
.photo{background:linear-gradient(180deg,#cdd3d8,#9aa4ad)}
.featured .photo{position:absolute;left:0;top:0;width:240px;height:388px}
.featured .info{position:absolute;left:288px;top:10px;width:592px}
.featured h3{font-size:25px;font-weight:600;color:#222;white-space:nowrap}
.featured .role{font-size:15px;font-weight:600;color:var(--blue);margin-top:6px}
.featured .bio{font-size:13px;color:var(--muted);line-height:1.7;margin-top:14px}
.featured .actions{position:absolute;left:288px;top:330px;display:flex;align-items:center;gap:20px}
.btn{display:inline-block;background:var(--maroon);color:#fff;font-size:13px;font-weight:700;text-transform:uppercase;padding:14px 34px;border-radius:30px;letter-spacing:.5px}
.mail{display:flex;align-items:center;gap:6px;font-size:12px;color:#555}

/* team grid */
.team-grid{position:absolute;top:1320px;left:112px;width:976px;display:flex;gap:16px}
.member{width:232px;height:530px;position:relative}
.member .photo{height:260px}
.member h4{font-size:15px;font-weight:600;color:#222;margin-top:16px}
.member .role{font-size:13px;font-weight:600;color:var(--blue);margin-top:6px;line-height:1.4}
.member .bio{font-size:12px;color:var(--muted);line-height:1.65;margin-top:10px}
.member .mail{position:absolute;left:0;bottom:0;width:232px;border-top:1px solid var(--line);padding-top:8px}

/* banner */
.cta-band{position:absolute;top:1940px;left:0;width:1200px;height:440px;background:linear-gradient(90deg,#e9b7a5 0%,#b03a3a 42%,var(--maroon) 60%,var(--maroon-dark))}
.cta-band .visual{position:absolute;left:0;top:0;width:520px;height:440px;background:linear-gradient(90deg,#f1c9b7,#d58c7a 70%,rgba(176,58,58,0))}
.cta-band h3{position:absolute;left:580px;top:110px;width:560px;color:#fff;font-size:32px;font-weight:600;line-height:1.3}
.cta-band .btn-outline{position:absolute;left:580px;top:275px;border:2px solid #fff;color:#fff;font-size:13px;font-weight:700;padding:12px 30px;border-radius:30px;text-transform:uppercase}

/* appointment */
.appointment{position:absolute;top:2420px;left:0;width:1200px;text-align:center}
.form-card{position:absolute;top:2530px;left:140px;width:940px;height:660px;background:#fff;box-shadow:0 4px 20px rgba(0,0,0,.15);border-radius:6px}
.form-card h3{position:absolute;left:24px;top:24px;font-size:22px;font-weight:600;color:#222}
.form-card .visual{position:absolute;right:14px;top:14px;width:280px;height:632px;border-radius:4px;background:linear-gradient(180deg,#bcdcf0,#e9dccb 60%,#d8c3a5)}
.form{position:absolute;left:24px;top:74px;width:600px}
.row{display:flex;gap:12px;margin-bottom:12px}
.field{flex:1;height:40px;border:1px solid #ccc;border-radius:3px;font-size:13px;color:#444;padding:10px 12px}
.label{font-size:13px;font-weight:600;color:#222;margin:10px 0 8px}
.opt{display:flex;gap:8px;align-items:flex-start;font-size:12px;color:#555;line-height:1.4}
.opt i{flex:none;width:14px;height:14px;border:1px solid #999;margin-top:1px}
.opt i.r{border-radius:50%}
.opts{display:grid;grid-template-columns:1fr 1fr;gap:12px 20px;width:560px}
.textarea{height:110px;border:1px solid #ccc;border-radius:3px;font-size:13px;color:#444;padding:10px 12px;margin-top:14px}
.form .btn{margin-top:20px;padding:13px 30px}

/* footer */
.site-footer{position:absolute;top:3330px;left:0;width:1200px;height:462px;background:var(--footer);color:#ccc}
.site-footer svg.curve{position:absolute;top:-1px;left:0;width:1200px;height:70px}
.site-footer .brand{position:absolute;left:40px;top:200px;color:#fff;font-size:46px}
.foot-col{position:absolute;top:118px;font-size:14px;line-height:1.75}
.foot-col h5{font-size:16px;font-weight:600;color:#fff;margin-bottom:10px}
.foot-col .ci{display:flex;gap:12px;align-items:center;margin-bottom:14px}
.foot-col .ci span.dot{width:30px;height:30px;border-radius:50%;border:1px solid #888;display:flex;align-items:center;justify-content:center}
.foot-col .ci .ico{fill:#ccc;width:13px;height:13px}
.copy{position:absolute;left:0;bottom:0;width:1200px;height:54px;border-top:1px solid #3a3536;font-size:12px;color:#aaa;padding:18px 40px}
.social{position:absolute;right:40px;top:13px;display:flex;gap:8px}
.social i{width:26px;height:26px;border-radius:50%;border:1px solid #777}
</style>
</head>
<body>

<header class="site-header">
  <a class="brand" href="#">Quintela.pro</a>
  <div class="topbar">
    <span><svg class="ico" viewBox="0 0 24 24"><path d="M2 5h20v14H2z M2 5l10 8 10-8" fill="none" stroke="#7b1d1d" stroke-width="2"/></svg>consulta@quintela.pro</span>
    <span><svg class="ico" viewBox="0 0 24 24"><path d="M6.6 10.8a15 15 0 006.6 6.6l2.2-2.2a1 1 0 011-.25 11.4 11.4 0 003.6.57 1 1 0 011 1V20a1 1 0 01-1 1A17 17 0 013 4a1 1 0 011-1h3.5a1 1 0 011 1c0 1.25.2 2.45.57 3.6a1 1 0 01-.25 1z"/></svg>(11) 4000-1234</span>
  </div>
  <nav class="main-nav">
    <a href="#">Home</a>
    <a href="#">About us</a>
    <a class="current" href="#">The team</a>
    <a href="#">News</a>
    <a href="#">Contact</a>
  </nav>
</header>

<section class="hero" role="img" aria-label="Surgeons in an operating room">
  <h1>TEAM</h1>
  <div class="dots"><i></i><i></i><i></i><i></i></div>
  <svg class="curve" viewBox="0 0 1200 120" preserveAspectRatio="none">
    <path d="M0 120 L0 70 C300 130 700 20 1200 40 L1200 120Z" fill="#fff"/>
    <path d="M0 60 C300 120 700 10 1200 30 L1200 40 C700 22 300 132 0 72Z" fill="#7b1d1d"/>
  </svg>
</section>

<section class="team-intro">
  <div class="section-title">The <b>Team</b></div>
  <h2>About us: Vascular Surgery Team, Endovascular, Ultrasound, Angiology</h2>
  <p>Complete vascular surgery team in São Paulo, SP. Several skilled professionals and the most advanced technology.</p>
  <p>Quintela.pro has several professionals who, together, are able to provide a differentiated and updated service, always counting on the most modern technology and ready to solve your problem! Vascular and Endovascular Surgery can hardly be performed alone. First, the bigger and better the team, the faster the surgery and less risk. And secondly, a multidisciplinary team with varied experiences expands the possibilities of treatments. Meet our team.</p>
</section>

<section class="featured">
  <div class="photo" role="img" aria-label="Portrait of the lead vascular surgeon"></div>
  <div class="info">
    <h3>Prof. Dr. Henrique Duarte Lemos Quintela</h3>
    <div class="role">Physician, Vascular and Endovascular and Ultrasound Surgeon</div>
    <p class="bio">Vascular, Endovascular and Vascular Ultrasound Surgery.<br>PhD in Medicine. Former assistant physician at a university hospital abroad. Specialist in Vascular and Endovascular Surgery by the national society of the specialty. Assistant Professor of Vascular Surgery at a São Paulo medical school. CRM 000001.</p>
    <p class="bio">Doctor, PhD in Science and MBA in Health Management, with years of teaching and clinical practice.</p>
  </div>
  <div class="actions">
    <a class="btn" href="#">Read more</a>
    <span class="mail"><svg class="ico" viewBox="0 0 24 24"><rect x="2" y="5" width="20" height="14"/></svg>dr.henrique@quintela.pro</span>
  </div>
</section>

<section class="team-grid">
  <article class="member">
    <div class="photo" role="img" aria-label="Portrait of a vascular surgeon"></div>
    <h4>Prof. Dr. Renato Quintela</h4>
    <div class="role">Angiology, Vascular and Endovascular Surgery</div>
    <p class="bio">Former foreign assistant at a surgical clinic in Europe. PhD in Sciences. Past member of the board of a regional medical academy. Titular Professor of Vascular Surgery with decades of practice in the field. CRM 000002.</p>
    <span class="mail"><svg class="ico" viewBox="0 0 24 24"><rect x="2" y="5" width="20" height="14"/></svg>renato@quintela.pro</span>
  </article>
  <article class="member">
    <div class="photo" role="img" aria-label="Portrait of a neurosurgeon"></div>
    <h4>Drª. Marina Quintela</h4>
    <div class="role">Neurosurgery</div>
    <p class="bio">Physician and neurosurgeon trained in São Paulo. Member of the national society of neurosurgery. Works with minimally invasive spine surgery and brain vascular care at partner hospitals. CRM 000003.</p>
    <span class="mail"><svg class="ico" viewBox="0 0 24 24"><rect x="2" y="5" width="20" height="14"/></svg>marina@quintela.pro</span>
  </article>
  <article class="member">
    <div class="photo" role="img" aria-label="Portrait of a vascular surgeon"></div>
    <h4>Drª. Helena Barros</h4>
    <div class="role">Vascular and Endovascular Surgery</div>
    <p class="bio">Assistant Professor of Vascular Surgery. Master of Science. Specialist in Angiology and Vascular Surgery, and in Angioradiology and Endovascular Surgery. CRM 000004.</p>
    <span class="mail"><svg class="ico" viewBox="0 0 24 24"><rect x="2" y="5" width="20" height="14"/></svg>helena@quintela.pro</span>
  </article>
  <article class="member">
    <div class="photo" role="img" aria-label="Portrait of a plastic surgeon"></div>
    <h4>Dr. Tomás Quintela</h4>
    <div class="role">Dr. Tomás Quintela</div>
    <p class="bio">Plastic surgeon certified by the national society. Graduated in Medicine in São Paulo. CRM 000005.</p>
    <span class="mail"><svg class="ico" viewBox="0 0 24 24"><rect x="2" y="5" width="20" height="14"/></svg>dr.tomas@quintela.pro</span>
  </article>
</section>

<section class="cta-band">
  <div class="visual" role="img" aria-label="Leg receiving a vascular treatment"></div>
  <h3>Aneurysm surgery, carotid stenosis, laser varicose veins and other vascular diseases</h3>
  <a class="btn-outline" href="#">Contact us now</a>
</section>

<section class="appointment">
  <div class="section-title">Schedule an <b>Appointment</b></div>
</section>

<section class="form-card">
  <h3>Contact Form</h3>
  <div class="form">
    <div class="row"><div class="field">Name :</div><div class="field">Email :</div></div>
    <div class="row"><div class="field">Phone No:</div><div class="field">City State Country :</div></div>
    <div class="label">Service Location :</div>
    <div class="opt"><i class="r"></i>Quintela - Institute of Advanced Medicine - São Paulo / SP</div>
    <div class="label">Area of Interest :</div>
    <div class="opts">
      <div class="opt"><i></i>Treatment of varicose veins with laser / Endovenous</div>
      <div class="opt"><i></i>Optimized treatment of carotid stenosis</div>
      <div class="opt"><i></i>Lipedema Treatment</div>
      <div class="opt"><i></i>Fibroid embolization</div>
      <div class="opt"><i></i>Advanced endovascular treatment of aneurysms</div>
      <div class="opt"><i></i>Others</div>
    </div>
    <div class="textarea">Message :</div>
    <a class="btn" href="#">Submit</a>
  </div>
  <div class="visual" role="img" aria-label="Couple walking on a beach"></div>
</section>

<footer class="site-footer">
  <svg class="curve" viewBox="0 0 1200 70" preserveAspectRatio="none">
    <path d="M0 0 H1200 V20 C800 70 400 0 0 40Z" fill="#fff"/>
    <path d="M0 40 C400 0 800 70 1200 20 V30 C800 80 400 10 0 50Z" fill="#7b1d1d"/>
  </svg>
  <div class="brand">Quintela.pro</div>
  <div class="foot-col" style="left:580px">
    <h5>Quick Links</h5>
    <a href="#">Home</a><br>
    <a href="#">About us</a><br>
    <a href="#">The team</a><br>
    <a href="#">News</a><br>
    <a href="#">Contact</a>
  </div>
  <div class="foot-col" style="left:756px">
    <h5>Contact Information</h5>
    <div class="ci"><span class="dot"><svg class="ico" viewBox="0 0 24 24"><path d="M12 2a7 7 0 00-7 7c0 5 7 13 7 13s7-8 7-13a7 7 0 00-7-7zm0 9.5A2.5 2.5 0 1112 6.5a2.5 2.5 0 010 5z"/></svg></span>Rua Alameda Prado, 1180, São Paulo, SP</div>
    <div class="ci"><span class="dot"><svg class="ico" viewBox="0 0 24 24"><path d="M6.6 10.8a15 15 0 006.6 6.6l2.2-2.2a1 1 0 011-.25 11.4 11.4 0 003.6.57 1 1 0 011 1V20a1 1 0 01-1 1A17 17 0 013 4a1 1 0 011-1h3.5a1 1 0 011 1c0 1.25.2 2.45.57 3.6a1 1 0 01-.25 1z"/></svg></span>(11) 4000-1234</div>
    <div class="ci"><span class="dot"><svg class="ico" viewBox="0 0 24 24"><rect x="2" y="5" width="20" height="14"/></svg></span>secretaria@quintela.pro</div>
  </div>
  <div class="copy">Copyright © 2020, Quintela.pro, All rights reserved.
    <div class="social"><i></i><i></i><i></i></div>
  </div>
</footer>

</body>
</html>
```